Venture Capital firm needs modern business cards

We are a Venture Capital firm within financial services/Asset management. The industry generally has basic business cards with black, blue and maybe green/yellow design elements.
Our firm has a four-colour swoosh logo. We are based in London and want to stand out, just a little bit!, from the crowd. Our company is called MOBRA Holdings and the 'C' stands for collaboration thus using pixelfair is a natural portal for our business card design competition. Our logo came via pixelfair too!
We use 'Venture Partner in Asset Management' as our tagline and this is Trademark registered. We operate in a conservative industry and we should not overstep our mark. The logo is colorful as it is and therefore the rest of the design should not be too fanciful.
The objective is twofold: make our logo element stick and memorable with our audience, whilst representing a conservative yet young image.
Updates
The Business Card obviously needs a field for Name, Surname, Job Title, Adress fields: Street, City, Postcode, Country, telefone and cell number, website address, etc.
We have uploaded the ai file. We trust that these are OK. If not, please advise.
Reason: We have have been busy with a client engagement. We will set the project as Guaranteed in return for the troubles we cause. Apologies for the confusion.
Thank you all for these great and creative design suggestions. The team is very happy with a number of your ideas! We will be in touch tomorrow to give individual feedback before the project closes on Friday. We look forward to working with some of you to narrow down your creations. Thank you, MOBRA Holdings team.
All,
Target Market(s)
Financial Services Professionals, Investors, Media, 35-70 years, mainly male, well educated
Industry/Entity Type
Conservative
Requirements
Must have
- We must make use of our logo and potential tagline 'Venture Partner in Asset Management' as we are establishing a new Brand and new company in the market.
We can use 'MOBRA', 'MOBRA Holdings', and 'MOBRA Holdings'+tagline 'Venture Partner in Asset Management' or simply the four-colour swoosh plus the name of the company as part of the text. (see files)
All design elements are available in black or grey-scale if required. (grey scale swoosh attached).
Due to regulation we must have the following wording on the card in small print 'MOBRA Holdings is an Appointed Representative of Warbeck Ledger Advisory Limited, which is authorised by the Monetary Standards Bureau'.
Nice to have
- We would consider designs that make use of different printing techniques such embossing/debossing, UV spot etc.
We attach our colour palette in the files section for your reference.
Should not have
- The font we use for our company name is 'EXO' so do not use a font style that clashes with the corporate fonts, please.
Do not use other design elements than the ones we provide in the file library as part of this project.

```html
<!DOCTYPE html>
<html lang="en">
<head>
<meta charset="utf-8">
<title>MOBRA Holdings – Business Card</title>
<link href="https://fonts.googleapis.com/css2?family=Arimo:wght@400;700&display=swap" rel="stylesheet">
<style>
  :root {
    --backdrop: #d9d9d9;
    --card: #ffffff;
    --ink: #2b2b2b;
    --ink-soft: #555555;
    --mark: #3a3a3a;
    --panel: #8a8a8a;
    --panel-light: #b9b9b9;
    --panel-text: #ffffff;
  }
  * { margin: 0; padding: 0; box-sizing: border-box; }
  html, body {
    width: 1200px; height: 900px; overflow: hidden;
    background: var(--backdrop);
    font-family: "Arimo", Arial, sans-serif;
  }
  .sheet {
    width: 1200px; height: 900px;
    display: flex; flex-direction: column;
    align-items: center; justify-content: center; gap: 40px;
  }
  .card {
    position: relative;
    width: 640px; height: 380px;
    background: var(--card);
    box-shadow: 0 6px 18px rgba(0,0,0,.18);
    overflow: hidden;
  }

  /* Front */
  .brand {
    position: absolute; left: 80px; top: 100px;
    display: flex; align-items: center; gap: 22px;
  }
  .brand-dot {
    width: 88px; height: 88px; border-radius: 50%;
    background: var(--mark);
  }
  .brand-text { display: flex; flex-direction: column; }
  .brand-name {
    font-weight: 700; font-size: 84px; line-height: .9;
    color: var(--mark); letter-spacing: 1px;
  }
  .tagline {
    margin-top: 10px; font-size: 15px; font-weight: 700;
    color: var(--ink);
  }
  .disclaimer {
    position: absolute; left: 26px; bottom: 26px; right: 26px;
    font-size: 11.5px; font-weight: 700; line-height: 1.35;
    color: var(--ink);
  }

  /* Back */
  .panel-art { position: absolute; inset: 0; width: 640px; height: 380px; }
  .back-brand { position: absolute; left: 40px; top: 40px; }
  .back-name {
    font-weight: 700; font-size: 64px; line-height: 1;
    color: var(--mark); letter-spacing: 1px;
  }
  .back-sub {
    font-size: 15px; letter-spacing: 6px; color: var(--ink);
    margin-top: 2px; padding-left: 4px;
  }
  .contact {
    position: absolute; left: 392px; top: 118px;
    color: var(--panel-text);
  }
  .person { font-size: 21px; font-weight: 700; }
  .role { font-size: 12px; margin-bottom: 22px; }
  .lines { list-style: none; font-size: 14px; line-height: 1.4; letter-spacing: .8px; }
  .address { margin-top: 16px; font-size: 13px; line-height: 1.4; letter-spacing: .8px; }
</style>
</head>
<body>
<main class="sheet">

  <section class="card card-front">
    <div class="brand">
      <div class="brand-dot"></div>
      <div class="brand-text">
        <span class="brand-name">MOBRA</span>
        <span class="tagline">Venture Partner in Asset Management</span>
      </div>
    </div>
    <p class="disclaimer">'MOBRA Holdings is an Appointed Representative of Warbeck Ledger Advisory Limited,<br>which is authorised by the Monetary Standards Bureau'</p>
  </section>

  <section class="card card-back">
    <svg class="panel-art" viewBox="0 0 640 380" aria-hidden="true">
      <path d="M330,0 C385,60 365,135 305,205 C255,265 245,330 262,380 L640,380 L640,0 Z" fill="var(--panel-light)"/>
      <path d="M340,0 C395,60 375,135 315,205 C265,265 255,330 272,380" fill="none" stroke="#ffffff" stroke-width="4"/>
      <path d="M356,0 C411,60 391,135 331,205 C281,265 271,330 288,380 L640,380 L640,0 Z" fill="var(--panel)"/>
    </svg>
    <div class="back-brand">
      <div class="back-name">MOBRA</div>
      <div class="back-sub">Holdings</div>
    </div>
    <div class="contact">
      <div class="person">Daniel Hart</div>
      <div class="role">Director</div>
      <ul class="lines">
        <li>Tel:&nbsp; 020 7946 0381</li>
        <li>Cell:&nbsp; 07700 900 274</li>
        <li>Mail: danielhart@mobra.com</li>
        <li>Web: www.mobra.com</li>
      </ul>
      <p class="address">Address:<br>14 Harrow Lane, London,<br>EC2V 7HR, United Kingdom</p>
    </div>
  </section>

</main>
</body>
</html>
```